New Wedding Decor Web Design Project - GUARANTEED PAYMENT

We need to have a business website for a brand new wedding decor & events company, Lirovelle. We have just established our logo and would love to use this logo on the website.

Because this is a new business venture, we do not have too many pictures to post online. It'd be exciting what your creativity can bring us!

Our website is: www.Lirovelle.ca

Target Market(s)

Our clientele demographic is targeted to brides and bridesmaids in their 20-30 years old.

Industry/Entity Type

Wedding

Requirements
Must have
• - Professional, elegant and artistic look
- Modern feeling
- Very catchy flash intro page
- Ability to show Chatterbook posts
Nice to have
• - Easy to navigate, crisp and clean
- Live vocaline messaging or online messaging

I would like to have navigation pages like: Lirovelle Brand, Collections, Features, Contact Us, etc.

Each page I want it to be clean and easy to read. Something like the following website: http://www.pardunetho.com/

We offer:
BACKDROPS
HEAD, CAKE & RECEIVING TABLES DECOR
CHAIRCOVERS
TABLE CLOTHS & OVERLAYS
NAPKINS
CENTREPIECES
CEREMONY SET-UP
CANDELABRA
CRYSTAL GLOBES
LED LIGHTING
CUSTOM DESIGN AISLE RUNNERS
CAKE STANDS
MONEY BOX
CHARGERS
GOBO LIGHTING
Should not have
• - traditional, old style website
- very static (dull)
- too many images or busy layout
- no "standardized" website templates such as: www.brintaq.com/gallery/weddings

```html
<!DOCTYPE html>
<html lang="en">
<head>
<meta charset="utf-8">
<title>Lirovelle Wedding Events</title>
<link rel="stylesheet" href="https://fonts.googleapis.com/css2?family=Roboto+Condensed:wght@500;700&family=Italianno&family=Arimo:wght@400;700&display=swap">
<style>
:root{
  --page-bg:#f1f0f6;
  --footer-top:#f4f3f9;
  --footer-bottom:#e9e6f4;
  --brand-purple:#5b35a6;
  --nav-active:#6a3aa8;
  --nav-text:#3b3a40;
  --list-text:#6b6a70;
  --muted:#9a99a0;
  --logo-pink:#e0469a;
  --logo-grey:#8c8b90;
  --chat-bg:#4a4a4c;
  --social:#9b98a8;
  --white:#ffffff;
}
*{margin:0;padding:0;box-sizing:border-box}
html,body{width:1200px;height:934px;overflow:hidden}
body{position:relative;background:var(--page-bg);font-family:"Arimo",Arial,sans-serif}
.topbar{position:absolute;left:0;top:0;width:1200px;height:54px;background:var(--page-bg)}
.social{position:absolute;display:flex;gap:8px}
.social span{width:16px;height:16px;border-radius:3px;background:var(--social)}
.social--top{left:940px;top:25px}
.social--footer{left:1033px;top:754px}
.top-divider{position:absolute;left:1010px;top:23px;width:1px;height:20px;background:#b5b3bd}
.live-chat{position:absolute;left:1019px;top:20px;width:78px;height:23px;background:var(--chat-bg);border-radius:2px;color:var(--white);font:700 11px "Arimo",Arial,sans-serif;line-height:23px;padding-left:6px}
.live-chat::after{content:"";position:absolute;right:8px;top:6px;width:10px;height:10px;border-radius:50%;background:#c8a27a}
.hero{position:absolute;left:0;top:54px;width:1200px;height:692px}
.photo{position:absolute;width:600px;height:346px}
.photo--hall{left:0;top:0;background:
  radial-gradient(ellipse 60% 40% at 45% 30%,rgba(235,225,240,.55),transparent 70%),
  linear-gradient(180deg,#b9aebf 0%,#9c8fa6 40%,#6f6276 75%,#4e4457 100%)}
.photo--lounge{left:600px;top:0;background:
  radial-gradient(ellipse 40% 55% at 20% 45%,rgba(220,190,245,.7),transparent 70%),
  radial-gradient(ellipse 50% 40% at 70% 30%,rgba(160,120,220,.5),transparent 70%),
  linear-gradient(180deg,#7d55c4 0%,#5e32a8 55%,#40227c 100%)}
.photo--head-table{left:0;top:346px;background:
  radial-gradient(ellipse 45% 30% at 60% 55%,rgba(245,215,240,.75),transparent 70%),
  radial-gradient(ellipse 30% 40% at 15% 25%,rgba(210,195,235,.5),transparent 70%),
  linear-gradient(180deg,#8a70b8 0%,#7a5aa4 45%,#6a3f7e 75%,#3c1f3e 100%)}
.photo--reception{left:600px;top:346px;background:
  radial-gradient(ellipse 60% 35% at 50% 20%,rgba(240,238,242,.8),transparent 70%),
  radial-gradient(ellipse 40% 20% at 65% 60%,rgba(190,70,90,.35),transparent 70%),
  linear-gradient(180deg,#cfcdd2 0%,#9e9ca2 50%,#5e5c62 100%)}
.logo-card{position:absolute;left:96px;top:52px;width:203px;height:87px;background:var(--white);box-shadow:0 1px 3px rgba(0,0,0,.2)}
.logo-mark{position:absolute;left:128px;top:30px;width:52px;height:52px;border-radius:50%;background:var(--logo-pink)}
.logo-name{position:absolute;left:111px;top:86px;font:400 30px "Arimo",Arial,sans-serif;letter-spacing:-.5px;color:var(--logo-grey)}
.logo-tagline{position:absolute;left:196px;top:120px;font:400 11px "Arimo",Arial,sans-serif;color:#a09fa6}
.main-nav{position:absolute;left:505px;top:85px;width:592px;height:54px;background:rgba(255,255,255,.88);box-shadow:0 1px 4px rgba(0,0,0,.25)}
.main-nav a{font:700 19px "Roboto Condensed","Arial Narrow",sans-serif;color:var(--nav-text);text-decoration:none;position:absolute;top:15px}
.main-nav a.is-active{color:var(--nav-active)}
.nav-sep{position:absolute;top:20px;height:14px;border-left:1px dotted #a5a3ab}
.tagline-box{position:absolute;left:97px;top:259px;width:504px;height:187px;background:rgba(20,16,24,.62)}
.tagline{position:absolute;left:0;top:26px;width:100%;text-align:center;font:400 70px/66px "Italianno",cursive;color:var(--white);text-shadow:2px 2px 4px rgba(0,0,0,.6)}
.tagline span{display:block}
.tagline .tagline-second{letter-spacing:6px}
.offers{position:absolute;left:0;top:746px;width:1200px;height:188px;background:linear-gradient(var(--footer-top),var(--footer-bottom))}
.offers h2{position:absolute;left:96px;top:4px;font:700 22px "Arimo",Arial,sans-serif;color:var(--brand-purple)}
.offer-list{position:absolute;top:39px;list-style:none}
.offer-list li{font:400 12px/18px "Arimo",Arial,sans-serif;color:var(--list-text);position:relative;padding-left:15px}
.offer-list li::before{content:"";position:absolute;left:2px;top:7px;width:3px;height:3px;border-radius:50%;background:var(--list-text)}
.offer-list--left{left:96px}
.offer-list--right{left:399px}
.footer-mark{position:absolute;left:1014px;top:126px;width:28px;height:28px;border-radius:50%;background:#b5b4b9}
.footer-name{position:absolute;left:1008px;top:154px;font:400 18px "Arimo",Arial,sans-serif;color:var(--logo-grey)}
.footer-tagline{position:absolute;left:1052px;top:174px;font:400 7px "Arimo",Arial,sans-serif;color:#a8a7ad}
.copyright{position:absolute;left:0;top:170px;width:1194px;text-align:center;font:400 11px "Arimo",Arial,sans-serif;color:var(--muted)}
</style>
</head>
<body>
<header class="topbar">
  <div class="social social--top" aria-label="Social links"><span></span><span></span><span></span></div>
  <div class="top-divider"></div>
  <div class="live-chat">Live Chat</div>
</header>

<section class="hero">
  <div class="photo photo--hall" role="img" aria-label="Reception hall with draped ceiling and covered chairs"></div>
  <div class="photo photo--lounge" role="img" aria-label="Cocktail tables with purple uplighting and drapes"></div>
  <div class="photo photo--head-table" role="img" aria-label="Lit head table with white draping"></div>
  <div class="photo photo--reception" role="img" aria-label="Banquet tables with white drapes and red floral centrepieces"></div>
  <div class="tagline-box">
    <h1 class="tagline"><span>The Best Wedding</span><span class="tagline-second">Decorater</span></h1>
  </div>
</section>

<div class="logo-card"></div>
<div class="logo-mark"></div>
<div class="logo-name">Lirovelle</div>
<div class="logo-tagline">wedding events</div>

<nav class="main-nav">
  <a class="is-active" href="#" style="left:19px">Home</a>
  <span class="nav-sep" style="left:82px"></span>
  <a href="#" style="left:99px">Lirovelle Brand</a>
  <span class="nav-sep" style="left:250px"></span>
  <a href="#" style="left:268px">Collections</a>
  <span class="nav-sep" style="left:373px"></span>
  <a href="#" style="left:392px">Features</a>
  <span class="nav-sep" style="left:479px"></span>
  <a href="#" style="left:498px">Contact Us</a>
</nav>

<footer class="offers">
  <h2>We Offer:</h2>
  <ul class="offer-list offer-list--left">
    <li>BACKDROPS</li>
    <li>HEAD, CAKE &amp; RECEIVING TABLES DECOR</li>
    <li>CHAIRCOVERS</li>
    <li>TABLE CLOTHS &amp; OVERLAYS</li>
    <li>NAPKINS</li>
    <li>CENTREPIECES</li>
    <li>CEREMONY SET-UP</li>
    <li>CANDELABRA</li>
  </ul>
  <ul class="offer-list offer-list--right">
    <li>CRYSTAL GLOBES</li>
    <li>LED LIGHTING</li>
    <li>CUSTOM DESIGN AISLE RUNNERS</li>
    <li>CAKE STANDS</li>
    <li>MONEY BOX</li>
    <li>CHARGERS</li>
    <li>GOBO LIGHTING</li>
  </ul>
  <div class="footer-mark"></div>
  <div class="footer-name">Lirovelle</div>
  <div class="footer-tagline">wedding events</div>
  <p class="copyright">Copyright © 2013 Vantory, Inc. All rights reserved.</p>
</footer>
<div class="social social--footer" aria-label="Social links"><span></span><span></span><span></span></div>
</body>
</html>
```